Business Card Design Project

We need a business card design for a relatively new company called Velmar Gear. We design paddle (an outdoor winter sport primarily played in the midwest and east coast) and tennis bags for women and men. Velmar Gear is a lifestyle brand for the next generation country club goers. Our bags merge fashion with functionality and are making country club sports trendier and more fashionable.

I would like to include space for
Name: (will fill this in for employees)
Velmar Gear
Phone: (will do this)
Email:
www.velmargear.example

Would also like to include Chatterbook and Flitter icons.
Please do not use pictures of the bags - this is just to give you an idea of what style bags we sell.

Target Market(s)

30 to 40 year old men and women - luxury market

Industry/Entity Type

Fashion

Requirements
Must have
• Would like the company logo included

```html
<!DOCTYPE html>
<html lang="en">
<head>
<meta charset="utf-8">
<title>Velmar Gear – Business Card</title>
<link rel="stylesheet" href="https://fonts.googleapis.com/css2?family=Arimo:wght@400;700&display=swap">
<style>
  :root {
    --ink: #242424;
    --paper: #f4e9cc;
    --orange: #ee7a1e;
    --red-orange: #e2491f;
    --yellow: #f2d020;
    --pale-yellow: #efdd85;
    --rule: rgba(70, 55, 30, 0.12);
  }
  * { box-sizing: border-box; margin: 0; padding: 0; }
  html, body {
    width: 1200px;
    height: 741px;
    overflow: hidden;
    background: var(--paper);
  }
  .business-card {
    position: relative;
    width: 1200px;
    height: 741px;
    overflow: hidden;
    font-family: "Arimo", Arial, sans-serif;
    color: var(--ink);
  }
  .marker-wash {
    position: absolute;
    inset: 0;
    background:
      radial-gradient(ellipse 70% 18% at 55% 8%, rgba(226, 73, 31, 0.55), transparent 70%),
      linear-gradient(180deg,
        var(--red-orange) 0%,
        var(--orange) 11%,
        #f3a322 21%,
        var(--yellow) 33%,
        var(--yellow) 50%,
        var(--pale-yellow) 62%,
        #f0dfa6 72%,
        var(--paper) 86%);
  }
  .ruled-lines {
    position: absolute;
    inset: 0;
    background: repeating-linear-gradient(180deg,
      transparent 0 33px,
      var(--rule) 33px 34px);
  }
  .contact {
    position: absolute;
    top: 166px;
    left: 0;
    width: 1146px;
    text-align: center;
  }
  .contact__name {
    font-size: 42px;
    font-weight: 700;
    letter-spacing: 0.3px;
    line-height: 1.1;
  }
  .contact__phone {
    margin-top: 6px;
    font-size: 24px;
    letter-spacing: 7px;
  }
  .contact__email {
    margin-top: 3px;
    font-size: 23px;
  }
  .contact__web {
    margin-top: 8px;
    font-size: 26px;
    letter-spacing: 8px;
  }
  .social {
    margin-top: 16px;
    display: flex;
    justify-content: center;
    gap: 34px;
    font-size: 18px;
    letter-spacing: 2px;
    list-style: none;
  }
  .social__item {
    display: flex;
    align-items: center;
    gap: 9px;
  }
  .social__dot {
    width: 12px;
    height: 12px;
    border-radius: 50%;
    background: var(--ink);
  }
  .brand {
    position: absolute;
    left: 28px;
    top: 508px;
    display: flex;
    align-items: center;
    gap: 38px;
  }
  .brand__mark {
    width: 176px;
    height: 176px;
    flex: none;
  }
  .brand__name {
    font-size: 156px;
    font-weight: 400;
    line-height: 1;
    color: var(--ink);
    white-space: nowrap;
  }
</style>
</head>
<body>
  <main class="business-card">
    <div class="marker-wash" role="img" aria-label="Loose orange and yellow marker strokes brushed across lightly ruled paper"></div>
    <div class="ruled-lines"></div>

    <section class="contact">
      <p class="contact__name">md.tarin solan mehrab</p>
      <p class="contact__phone">+880 01700555012</p>
      <p class="contact__email">tarinstudio@mailbox.example</p>
      <p class="contact__web">www.velmargear.example</p>
      <ul class="social">
        <li class="social__item"><span class="social__dot"></span>Chatterbook</li>
        <li class="social__item"><span class="social__dot"></span>Flitter</li>
      </ul>
    </section>

    <div class="brand">
      <svg class="brand__mark" viewBox="0 0 176 176" aria-hidden="true">
        <circle cx="88" cy="88" r="84" fill="var(--ink)"/>
      </svg>
      <span class="brand__name">Velmar Gear</span>
    </div>
  </main>
</body>
</html>
```